NEW YORK Plumbing/utility company 10 year anniversary business card

Looking For simple back and front business card would like to include a few things in description
We offer 24/7 emergency service
residential
commercial
industrial
municipal
services offered
Plumbing
hydro excavation
hydro jetting
Well pumps
Sewer pumps
water mains
sewer mains

```html
<!DOCTYPE html>
<html lang="en">
<head>
<meta charset="utf-8">
<title>Kessler Valley Water &amp; Sewer — Business Card</title>
<link href="https://fonts.googleapis.com/css2?family=Montserrat:wght@400;500;700;800&display=swap" rel="stylesheet">
<style>
  :root {
    --backdrop: #2b2b2d;
    --sky: #35a9e4;
    --sky-light: #5bbcef;
    --sky-deep: #1f8fd0;
    --ink: #0b0b0c;
    --ink-soft: #1c1c1e;
    --brand-blue: #2f86c9;
    --band-blue: #1f6fb6;
    --white: #ffffff;
    --grey-text: #d9d9d9;
  }
  * { box-sizing: border-box; margin: 0; padding: 0; }
  html, body {
    width: 1200px; height: 1186px; overflow: hidden;
    background: var(--backdrop);
    font-family: 'Montserrat', sans-serif;
  }
  .canvas { position: relative; width: 1200px; height: 1186px; }

  .card {
    position: absolute; left: 160px; width: 880px; height: 503px;
    border-radius: 34px; overflow: hidden;
    box-shadow: 0 18px 40px rgba(0,0,0,.45);
  }

  .wordmark {
    position: absolute; left: 0; right: 0;
    display: flex; align-items: center; justify-content: center; gap: 24px;
  }
  .wordmark-dot { width: 40px; height: 40px; border-radius: 50%; background: currentColor; flex: none; }
  .wordmark-name {
    font-weight: 800; font-size: 52px; line-height: 1.08; letter-spacing: 2px;
    text-transform: uppercase; text-align: center;
  }

  /* Front */
  .card-front {
    top: 60px;
    background: linear-gradient(120deg, var(--sky-light) 0%, var(--sky) 50%, var(--sky-deep) 100%);
    color: var(--white);
  }
  .card-front .wordmark { top: 100px; }

  .services {
    position: absolute; left: 50px; right: 50px; bottom: 78px;
    display: flex; flex-direction: column; align-items: center; gap: 22px;
    list-style: none; font-size: 21px; font-weight: 500;
  }
  .service-row { display: flex; gap: 34px; list-style: none; }
  .service-row li { display: flex; align-items: center; gap: 10px; white-space: nowrap; }
  .service-icon { width: 24px; height: 24px; flex: none; }

  /* Back */
  .card-back {
    top: 623px;
    background: linear-gradient(150deg, var(--ink-soft) 0%, var(--ink) 60%);
    color: var(--white);
  }
  .card-back .wordmark { top: 62px; color: var(--brand-blue); }

  .contact-row {
    position: absolute; left: 0; right: 0; top: 245px;
    display: flex; justify-content: center; align-items: center; gap: 30px;
  }
  .person { text-align: right; }
  .person-name { font-weight: 700; font-size: 34px; color: var(--sky); }
  .person-title { font-size: 20px; color: var(--grey-text); margin-top: 2px; }
  .divider { width: 2px; height: 74px; background: var(--band-blue); }
  .contact-list { list-style: none; font-size: 20px; color: var(--grey-text); }
  .contact-list li { display: flex; align-items: center; gap: 12px; line-height: 1.7; }
  .contact-icon { width: 20px; height: 20px; flex: none; }

  .sector-band {
    position: absolute; left: 0; right: 0; bottom: 34px; height: 62px;
    background: var(--band-blue);
    display: flex; justify-content: space-around; align-items: center;
    list-style: none; padding: 0 40px;
    font-weight: 700; font-size: 19px; letter-spacing: .5px; text-transform: uppercase;
  }
  .sector-band li::before {
    content: ""; display: inline-block; width: 9px; height: 9px; border-radius: 50%;
    background: var(--white); margin-right: 10px; vertical-align: middle;
  }
</style>
</head>
<body>
<svg width="0" height="0" style="position:absolute" aria-hidden="true">
  <symbol id="tools" viewBox="0 0 24 24">
    <circle cx="12" cy="12" r="12" fill="#fff"/>
    <path d="M7 7 L17 17 M17 7 L7 17" stroke="#35a9e4" stroke-width="2.6" stroke-linecap="round"/>
  </symbol>
</svg>

<main class="canvas">
  <section class="card card-front" aria-label="Card front">
    <div class="wordmark">
      <span class="wordmark-dot"></span>
      <span class="wordmark-name">Kessler Valley<br>Water &amp; Sewer</span>
    </div>
    <div class="services">
      <ul class="service-row">
        <li><svg class="service-icon"><use href="#tools"/></svg>Plumbing</li>
        <li><svg class="service-icon"><use href="#tools"/></svg>Hydro excavation</li>
        <li><svg class="service-icon"><use href="#tools"/></svg>Hydro jetting</li>
        <li><svg class="service-icon"><use href="#tools"/></svg>Well pumps</li>
      </ul>
      <ul class="service-row">
        <li><svg class="service-icon"><use href="#tools"/></svg>Sewer pumps</li>
        <li><svg class="service-icon"><use href="#tools"/></svg>Water mains</li>
        <li><svg class="service-icon"><use href="#tools"/></svg>Sewer mains</li>
      </ul>
    </div>
  </section>

  <section class="card card-back" aria-label="Card back">
    <div class="wordmark">
      <span class="wordmark-dot"></span>
      <span class="wordmark-name">Kessler Valley<br>Water &amp; Sewer</span>
    </div>
    <div class="contact-row">
      <div class="person">
        <p class="person-name">Dana Whitlock</p>
        <p class="person-title">Managing Director</p>
      </div>
      <span class="divider"></span>
      <ul class="contact-list">
        <li>
          <svg class="contact-icon" viewBox="0 0 20 20" aria-hidden="true"><path d="M4 2h4l1.5 4-2 1.5a11 11 0 0 0 5 5L14 10.5l4 1.5v4a2 2 0 0 1-2 2A14 14 0 0 1 2 4a2 2 0 0 1 2-2z" fill="#2f86c9"/></svg>
          845-555-0182
        </li>
        <li>
          <svg class="contact-icon" viewBox="0 0 20 20" aria-hidden="true"><rect x="1" y="4" width="18" height="12" rx="1.5" fill="#2f86c9"/><path d="M1.5 5l8.5 6 8.5-6" stroke="#0b0b0c" stroke-width="1.6" fill="none"/></svg>
          info@kesslervalley.com
        </li>
      </ul>
    </div>
    <ul class="sector-band">
      <li>Residential</li>
      <li>Commercial</li>
      <li>Industrial</li>
      <li>Municipal</li>
    </ul>
  </section>
</main>
</body>
</html>
```